Vegan bakery needs business card

We need a business card design for my vegan bakery in Ashford Vt. We create amazing whole food plant based cuisine that is egg and dairy free. We use fruits, vegetables, healing herbs, nuts, natural sugars (date, turbinado, agave) and non bleached flours in our creations. Due to demand and interest in the Philadelphia area we created a late night vegan dessert delivery service named Moonlark Greens. We are the only business providing delicious vegan desserts delivered to your door at 1am!! We would like to see designs that use the color scheme in the logo. The final design should communicate the benefits of our products: dairy/egg free, plant based, healing herbs, amazing food.

Industry/Entity Type

Business

```html
<!DOCTYPE html>
<html lang="en">
<head>
<meta charset="utf-8">
<title>Moonlark Greens – Business Card</title>
<link href="https://fonts.googleapis.com/css2?family=Mulish:wght@400;600;700&display=swap" rel="stylesheet">
<style>
  :root {
    --backdrop: #e8e8e8;
    --card-white: #ffffff;
    --leaf-green: #5dbd45;
    --leaf-green-deep: #52ad3c;
    --frame-green: #5cbb43;
    --coral: #ec7a5c;
    --text-white: #ffffff;
    --soft-blush: #fcf6f3;
  }
  * { box-sizing: border-box; margin: 0; padding: 0; }
  html, body { width: 1200px; height: 900px; overflow: hidden; }
  body {
    background: var(--backdrop);
    font-family: "Mulish", "Century Gothic", sans-serif;
    position: relative;
  }
  .card {
    position: absolute;
    top: 300px;
    width: 520px;
    height: 300px;
    border-radius: 26px;
    overflow: hidden;
    box-shadow: 0 10px 24px rgba(0,0,0,0.12);
  }
  /* Front */
  .card-front { left: 50px; background: var(--card-white); }
  .front-pattern {
    position: absolute; inset: 20px;
    border-radius: 20px;
    background: var(--soft-blush);
  }
  .front-frame {
    position: absolute; inset: 20px;
    border: 7px solid var(--frame-green);
    border-radius: 20px;
  }
  .front-content {
    position: absolute; inset: 0;
    display: flex; flex-direction: column; align-items: center; justify-content: center;
    padding-top: 10px;
  }
  .brand-mark { display: flex; align-items: center; gap: 12px; }
  .brand-dot { width: 26px; height: 26px; border-radius: 50%; background: var(--coral); }
  .brand-name {
    font-weight: 600; font-size: 38px; color: var(--coral); letter-spacing: 0.5px;
  }
  .tagline {
    margin-top: 26px; text-align: center;
    color: var(--leaf-green); font-size: 24px; font-weight: 400; line-height: 1.05;
  }
  /* Back */
  .card-back { left: 630px; background: var(--leaf-green); color: var(--text-white); }
  .back-pattern { position: absolute; inset: 0; background: var(--leaf-green-deep); opacity: 0.25; }
  .identity {
    position: absolute; left: 110px; top: 122px; width: 165px; text-align: right;
  }
  .person-name { font-weight: 700; font-size: 19px; }
  .person-role { font-size: 13px; margin-top: 4px; }
  .divider {
    position: absolute; left: 292px; top: 100px; width: 1px; height: 100px;
    background: rgba(255,255,255,0.85);
  }
  .contact-list {
    position: absolute; left: 308px; top: 106px; list-style: none;
    font-size: 11.5px; line-height: 1;
  }
  .contact-list li { display: flex; align-items: center; gap: 7px; margin-bottom: 6px; }
  .contact-list li.continued { padding-left: 19px; }
  .contact-list svg { width: 12px; height: 12px; fill: var(--text-white); flex: none; }
  .back-brand {
    position: absolute; left: 34px; top: 218px;
    display: flex; flex-direction: column; align-items: center;
  }
  .back-brand .brand-name { color: var(--text-white); font-size: 19px; }
  .back-brand .brand-dot { width: 14px; height: 14px; background: var(--text-white); }
  .back-brand .brand-mark { gap: 7px; }
  .back-tagline { margin-top: 8px; font-size: 13px; line-height: 1.05; color: var(--text-white); text-align: center; }
</style>
</head>
<body>
  <section class="card card-front">
    <div class="front-pattern" role="img" aria-label="Faint blush swirl ornament pattern"></div>
    <div class="front-frame"></div>
    <div class="front-content">
      <div class="brand-mark">
        <span class="brand-dot"></span>
        <span class="brand-name">Moonlark Greens</span>
      </div>
      <p class="tagline">100% vegan<br>100% delicious</p>
    </div>
  </section>

  <section class="card card-back">
    <div class="back-pattern" role="img" aria-label="Tone-on-tone green swirl ornament pattern"></div>
    <div class="identity">
      <p class="person-name">Dana Whitfield</p>
      <p class="person-role">Manager</p>
    </div>
    <div class="divider"></div>
    <ul class="contact-list">
      <li><svg viewBox="0 0 24 24"><path d="M6.6 10.8a15 15 0 0 0 6.6 6.6l2.2-2.2a1 1 0 0 1 1-.25 11.4 11.4 0 0 0 3.6.57 1 1 0 0 1 1 1V20a1 1 0 0 1-1 1A17 17 0 0 1 3 4a1 1 0 0 1 1-1h3.5a1 1 0 0 1 1 1c0 1.25.2 2.45.57 3.6a1 1 0 0 1-.25 1z"/></svg>(215) 555-0147</li>
      <li><svg viewBox="0 0 24 24"><path d="M2 5h20v14H2z M4 7v.5l8 5 8-5V7l-8 5z" fill-rule="evenodd"/></svg>dana@moonlarkgreens.com</li>
      <li><svg viewBox="0 0 24 24"><path d="M12 2a10 10 0 1 0 0 20 10 10 0 0 0 0-20zm0 2c.9 1.2 1.6 2.7 1.9 4.5h-3.8C10.4 6.7 11.1 5.2 12 4zM4.3 14a8 8 0 0 1 0-4h3.6a16 16 0 0 0 0 4zm.8 2h3.2c.4 1.4.9 2.6 1.6 3.6A8 8 0 0 1 5.1 16zm3.2-8H5.1a8 8 0 0 1 4.8-3.6c-.7 1-1.2 2.2-1.6 3.6zM12 20c-.9-1.2-1.6-2.7-1.9-4h3.8c-.3 1.3-1 2.8-1.9 4zm2.3-6H9.7a14 14 0 0 1 0-4h4.6a14 14 0 0 1 0 4zm-.2 5.6c.7-1 1.2-2.2 1.6-3.6h3.2a8 8 0 0 1-4.8 3.6zM16.1 14a16 16 0 0 0 0-4h3.6a8 8 0 0 1 0 4zm-.4-6c-.4-1.4-.9-2.6-1.6-3.6A8 8 0 0 1 18.9 8z"/></svg>www.moonlarkgreens.com</li>
      <li><svg viewBox="0 0 24 24"><path d="M12 3 1 12h3v9h6v-6h4v6h6v-9h3z"/></svg>4820 Orchard Lane, Ste 120</li>
      <li class="continued">Ashford Vt.</li>
    </ul>
    <div class="back-brand">
      <div class="brand-mark">
        <span class="brand-dot"></span>
        <span class="brand-name">Moonlark Greens</span>
      </div>
      <p class="back-tagline">100% vegan<br>100% delicious</p>
    </div>
  </section>
</body>
</html>
```